Real Estate Media Company Business Card

’m looking for a modern, high-end, double-sided business card for:
Brightpath Studio LLC
(Real Estate Photography & Videography)
The design should feel clean, minimal, and premium, appealing to top real estate agents and brokers.
👉 Horizontal layout is preferred
👉 Vertical option is welcome but not required
⸻
Front Side (Main Information):
Include:
* Tobias Wrenfield
* Brightpath Studio LLC
* Title (open to creative improvement)
* Phone Number
* Email
* Website
⸻
Services Section (VERY IMPORTANT):
This should be a key visual element, not an afterthought.
Services to Include:
* Cinematic Video
* Real Estate Photography
* Drone
* Social Media Reels
* Floor Plans
* Use clean, modern icons next to each service
* Icons should be simple, minimal, and consistent style (outline or thin line preferred)
* Option to place icons inside small circles (like reference)
Layout:
* Format services similar to a clean horizontal or grid-style list (like “example 2”)
* Keep spacing balanced and uncluttered
* Make this section visually appealing and easy to scan
⸻
Back Side:
* Keep it extremely minimal
* Only include the logo in a corner
* No additional text needed
⸻
Typography & Style:
* Modern, clean, slightly bold fonts (based on uploaded references)
* Strong hierarchy (name + services stand out most)
* Plenty of white/negative space
* Avoid clutter
⸻
Overall Feel:
* Luxury
* Modern
* Clean
* Confident
* High-end real estate branding
⸻
Notes for Designers:
* Simplicity is key
* Services section should feel polished and intentional
* This card should feel like something a top-producing real estate agent would keep
Real estate agent agents

```html
<!DOCTYPE html>
<html lang="en">
<head>
<meta charset="utf-8">
<title>Brightpath Studio – Business Card</title>
<link href="https://fonts.googleapis.com/css2?family=Ubuntu:wght@400;500&display=swap" rel="stylesheet">
<style>
  :root {
    --backdrop: #3b2f24;
    --card-black: #111111;
    --gold: #c8a862;
    --white: #ffffff;
  }
  * { margin: 0; padding: 0; box-sizing: border-box; }
  html, body { width: 1060px; height: 1200px; overflow: hidden; }
  body {
    background: var(--backdrop);
    font-family: "Ubuntu", sans-serif;
    position: relative;
  }
  .card {
    position: absolute;
    left: 160px;
    width: 740px;
    height: 422px;
    border-radius: 22px;
    overflow: hidden;
    background: var(--card-black);
    box-shadow: 0 8px 24px rgba(0,0,0,0.35);
  }
  .card-front { top: 109px; }
  .card-back { top: 618px; }

  .person-name {
    position: absolute; left: 37px; top: 30px;
    color: var(--white); font-size: 41px; font-weight: 500; line-height: 1;
  }
  .person-title {
    position: absolute; left: 37px; top: 78px;
    color: var(--gold); font-size: 25px; font-weight: 400; line-height: 1;
  }
  .company-name {
    position: absolute; left: 37px; top: 114px;
    color: var(--white); font-size: 28px; font-weight: 500; line-height: 1;
  }
  .services-divider {
    position: absolute; left: 356px; top: 159px;
    width: 2px; height: 156px; background: var(--gold);
  }
  .services-list { position: absolute; left: 381px; top: 152px; list-style: none; }
  .service-item {
    display: flex; align-items: center; height: 35.3px;
    color: var(--white); font-size: 24px;
  }
  .service-icon { width: 34px; height: 24px; margin-right: 13px; flex: none; }

  .contact-list { position: absolute; left: 38px; top: 309px; list-style: none; }
  .contact-item {
    display: flex; align-items: center; height: 32px;
    color: var(--gold); font-size: 21px;
  }
  .contact-icon { width: 24px; height: 24px; margin-right: 10px; flex: none; }

  .back-gold-panel {
    position: absolute; left: 0; top: 0; width: 100%; height: 276px;
    background: var(--gold);
  }
  .brand-name {
    position: absolute; left: 520px; top: 318px; width: 160px;
    color: var(--white); font-size: 20px; font-weight: 400;
    letter-spacing: 2px; text-align: center; line-height: 1.3;
  }
</style>
</head>
<body>
  <svg width="0" height="0" style="position:absolute">
    <defs>
      <symbol id="icon-camera" viewBox="0 0 34 24">
        <g fill="none" stroke="#c8a862" stroke-width="1.3">
          <rect x="1" y="5" width="32" height="18" rx="2"/>
          <path d="M11 5 L13 1.5 H21 L23 5"/>
          <circle cx="17" cy="14" r="6"/>
          <circle cx="17" cy="14" r="3.5"/>
          <rect x="3.5" y="2" width="5" height="3"/>
          <line x1="26" y1="9" x2="30" y2="9"/>
        </g>
      </symbol>
    </defs>
  </svg>

  <section class="card card-front">
    <h1 class="person-name">Tobias Wrenfield</h1>
    <p class="person-title">Founder | Real Estate Media Specialist</p>
    <p class="company-name">Brightpath Studio LLC</p>

    <div class="services-divider"></div>
    <ul class="services-list">
      <li class="service-item"><svg class="service-icon"><use href="#icon-camera"/></svg>Cinematic Video</li>
      <li class="service-item"><svg class="service-icon"><use href="#icon-camera"/></svg>Real Estate Photography</li>
      <li class="service-item"><svg class="service-icon"><use href="#icon-camera"/></svg>Drone</li>
      <li class="service-item"><svg class="service-icon"><use href="#icon-camera"/></svg>Social Media Reels</li>
      <li class="service-item"><svg class="service-icon"><use href="#icon-camera"/></svg>Floor Plans</li>
    </ul>

    <ul class="contact-list">
      <li class="contact-item">
        <svg class="contact-icon" viewBox="0 0 24 24"><path fill="#ffffff" d="M6.6 10.8a15.1 15.1 0 0 0 6.6 6.6l2.2-2.2a1 1 0 0 1 1-.25 11.4 11.4 0 0 0 3.6.57 1 1 0 0 1 1 1V20a1 1 0 0 1-1 1A17 17 0 0 1 3 4a1 1 0 0 1 1-1h3.5a1 1 0 0 1 1 1c0 1.25.2 2.45.57 3.57a1 1 0 0 1-.25 1z"/></svg>
        610-555-0142
      </li>
      <li class="contact-item">
        <svg class="contact-icon" viewBox="0 0 24 24"><path fill="#ffffff" d="M2 5h20v14H2z M3.5 6.5 12 13l8.5-6.5" stroke="#111111" stroke-width="1.4"/></svg>
        tobias@brightpathstudiopa.com
      </li>
      <li class="contact-item">
        <svg class="contact-icon" viewBox="0 0 24 24"><g fill="none" stroke="#ffffff" stroke-width="1.5"><circle cx="12" cy="12" r="10"/><ellipse cx="12" cy="12" rx="4.5" ry="10"/><line x1="2" y1="12" x2="22" y2="12"/><path d="M4 7h16M4 17h16"/></g></svg>
        www.brightpathstudiopa.com
      </li>
    </ul>
  </section>

  <section class="card card-back">
    <div class="back-gold-panel"></div>
    <p class="brand-name">BRIGHTPATH<br>STUDIO</p>
  </section>
</body>
</html>
```